Quick Straightforward Billboard Redesign

- Design billboard sized for 10 foot' x 36' foot width live area size and please include bleeds 6" around all sides
- Exact blue color match is imperative in headline, logo, phone number bubble or wherever used. C-83 / M-45 / Y-1 / K-0-
- What I hope to illustrate is that our company offers the best porch screening in the area area, in regards to quality, expertise, durability, storms proof, but we do not build screen porches.
- Current board is attached below from previous designer, and as you can see sizing was off, white space on edges make it appear to be sized incorrectly.
- I also attached my own little mock up idea well well if it helps, favorite image, logo, headline, etc and ideas perhaps on expanding or making this better?

Thanks so much!

Target Market(s)

Drivers and passengers, Southeastern NC, are of immense new construction and high end homes.

Industry/Entity Type

Construction

Colors
0054AA
0677BA
7BADD7
CADEEF
E8F1F8

Requirements
Must have
• Blue color matching
Nice to have
• Design spins or other thoughts on my little mock up

```html
<!DOCTYPE html>
<html lang="en">
<head>
<meta charset="utf-8">
<title>Harborline Screens Billboard</title>
<link rel="stylesheet" href="https://fonts.googleapis.com/css2?family=Bebas+Neue&family=Anton&display=swap">
<style>
  :root {
    --brand-blue: #0677BA;
    --deep-blue: #0054AA;
    --sky-blue: #7BADD7;
    --pale-blue: #CADEEF;
    --mist: #E8F1F8;
    --coast-green: #22A84F;
    --rule-grey: #cfd3d6;
    --white: #ffffff;
    --page: #ffffff;
  }
  * { margin: 0; padding: 0; box-sizing: border-box; }
  html, body {
    width: 1185px; height: 1200px; overflow: hidden;
    background: var(--page);
  }
  .canvas {
    position: relative; width: 1185px; height: 1200px;
    display: flex; align-items: center; justify-content: center;
  }
  .billboard {
    position: relative; width: 1105px; height: 307px; overflow: hidden;
    background: var(--white);
    box-shadow: 0 4px 10px rgba(0,0,0,0.18);
  }
  .sky-band {
    position: absolute; left: 0; top: 0; width: 100%; height: 188px;
    background: linear-gradient(180deg, #9fd8ef 0%, var(--mist) 70%, #f2f4f5 100%);
  }
  .porch-photo {
    position: absolute; right: 0; top: 0; width: 540px; height: 307px;
    background:
      linear-gradient(90deg, rgba(255,255,255,1) 0%, rgba(255,255,255,0) 22%),
      linear-gradient(180deg, #f3f3f0 0%, #e8e8e4 24%, #9cc3e6 30%, #8fbfe0 44%, #6f9a5c 52%, #8a8478 68%, #6e665c 100%);
  }
  .headline {
    position: absolute; left: 0; top: 26px;
    font-family: "Bebas Neue", "Anton", sans-serif;
    font-size: 80px; line-height: 68px; letter-spacing: 0.5px;
  }
  .headline-line { display: flex; align-items: center; height: 68px; }
  .headline-line::before {
    content: ""; display: block; width: 44px; height: 54px;
    border-radius: 0 8px 8px 0; margin-right: 18px;
  }
  .headline-line.screen { color: var(--brand-blue); }
  .headline-line.screen::before { background: var(--brand-blue); }
  .headline-line.coast { color: var(--coast-green); }
  .headline-line.coast::before { background: var(--coast-green); }
  .headline-line span {
    text-shadow: 2px 2px 0 var(--white), -1px -1px 0 var(--white), 3px 3px 2px rgba(0,0,0,0.15);
    padding-top: 8px;
  }
  .divider {
    position: absolute; left: 0; top: 179px; width: 400px; height: 5px;
    background: linear-gradient(90deg, var(--rule-grey) 0%, rgba(207,211,214,0) 100%);
  }
  .brand {
    position: absolute; left: 30px; top: 222px;
    display: flex; align-items: center; gap: 16px;
  }
  .brand-square { width: 40px; height: 40px; background: var(--brand-blue); }
  .brand-name {
    font-family: "Bebas Neue", "Anton", sans-serif;
    font-size: 60px; line-height: 1; color: var(--brand-blue); padding-top: 6px;
  }
  .phone-bar {
    position: absolute; left: 798px; top: 225px; width: 307px; height: 54px;
    background: var(--brand-blue);
    box-shadow: 0 3px 4px rgba(0,0,0,0.25);
    display: flex; align-items: center; padding-left: 30px;
    font-family: "Anton", "Bebas Neue", sans-serif;
    font-size: 36px; color: var(--white); letter-spacing: 1px;
  }
  .phone-badge {
    position: absolute; left: 741px; top: 217px; width: 70px; height: 70px;
    border-radius: 50%; background: var(--coast-green);
    border: 4px solid var(--white);
    box-shadow: 0 3px 5px rgba(0,0,0,0.3);
    display: flex; align-items: center; justify-content: center;
  }
</style>
</head>
<body>
<div class="canvas">
  <div class="billboard">
    <div class="sky-band"></div>
    <div class="porch-photo" role="img" aria-label="Photo of a screened porch with wicker lounge seating, ceiling fan and lake view"></div>

    <div class="headline">
      <div class="headline-line screen"><span>SCREEN YOUR PORCH.</span></div>
      <div class="headline-line coast"><span>BUILT FOR THE COAST.</span></div>
    </div>
    <div class="divider"></div>

    <div class="brand">
      <div class="brand-square"></div>
      <div class="brand-name">HARBORLINE SCREENS</div>
    </div>

    <div class="phone-bar">910.555.0142</div>
    <div class="phone-badge">
      <svg width="34" height="34" viewBox="0 0 24 24" aria-hidden="true">
        <path fill="#ffffff" d="M6.6 10.8a15.1 15.1 0 0 0 6.6 6.6l2.2-2.2c.3-.3.7-.4 1-.2 1.1.4 2.3.6 3.6.6.6 0 1 .4 1 1V20c0 .6-.4 1-1 1A17 17 0 0 1 3 4c0-.6.4-1 1-1h3.5c.6 0 1 .4 1 1 0 1.3.2 2.5.6 3.6.1.3 0 .7-.2 1L6.6 10.8z"/>
      </svg>
    </div>
  </div>
</div>
</body>
</html>
```